Orthopaedic Clinic Needs facebook page

Orthopaedic Clinic needs facebook page. The name of our clinic is Larchmont Orthopaedics. We focus on hip and knee orthopaedic conditions, as well as general orthopaedics. The main services are total knee replacements, total hip replacements, sports injury of the knee, hip fractures. Unique selling points of our service would be 1. Patient Centred Care, 2. Value Driven, 3. 2 Double-Fellowship Trained Surgeons.

Colour scheme should fit the logo design and be within the general colour recommendations of a medical clinic.

The design should be modern, eye catching, draws the end user to the website.

We would like to design our facebook page for future social media marketing.
In accordance with local advertisement regulations pertaining to medical clinics, no statements must have any information or laudatory statements such as the use of best, better, breakthrough, champions, or any statements that imply superiority and that may create unjustified expectations of services.

Target Market(s)

Patients
Friends family and relatives of patients.

Font styles to use
Serif
Sans Serif

Requirements
Must have
• My project must have my logo.

A nice colour scheme comfortable to the eye.
Nice to have
• Nice eye catching design that will draw the end user to the page.
Should not have
• Must not have any information that create unjustified expectaions.
Must not contain laudatory statements such as best, better, breakthrough, champions, or other statement that may create unjustified expecation of services.

```html
<!DOCTYPE html>
<html lang="en">
<head>
<meta charset="utf-8">
<title>Larchmont Orthopaedics – Cover</title>
<link rel="stylesheet" href="https://fonts.googleapis.com/css2?family=Josefin+Sans:wght@400&family=Montserrat:wght@600;700&display=swap">
<style>
  :root {
    --ink-dark: #0b2a33;
    --teal: #4fb3a9;
    --slate: #5b6670;
    --white: #ffffff;
    --caption-bg: rgba(11, 42, 51, 0.86);
  }
  * { box-sizing: border-box; margin: 0; padding: 0; }
  html, body { width: 1200px; height: 444px; overflow: hidden; background: var(--white); }
  .cover { position: relative; width: 1200px; height: 444px; background: var(--white); }

  .brand { position: absolute; left: 16px; top: 20px; display: flex; align-items: center; gap: 20px; }
  .brand-mark { width: 86px; height: 88px; background: var(--teal); border-radius: 6px; }
  .brand-name { font-family: "Josefin Sans", sans-serif; font-weight: 400; color: var(--slate); line-height: 1; }
  .brand-name .line-1 { display: block; font-size: 50px; letter-spacing: 1.5px; }
  .brand-name .line-2 { display: block; font-size: 29px; letter-spacing: 9.5px; margin-top: 8px; }

  .services-panel { position: absolute; left: 0; top: 129px; width: 477px; height: 222px; background: var(--ink-dark); }
  .services-box { position: absolute; left: 14px; top: 45px; width: 448px; height: 146px; border: 2px solid var(--white); border-radius: 8px; }
  .services-title {
    position: absolute; left: 26px; top: -21px; padding: 0 6px; background: var(--ink-dark);
    font-family: "Montserrat", sans-serif; font-weight: 700; font-size: 30px; color: var(--teal); letter-spacing: 1.5px; line-height: 1.2;
  }
  .services-list { list-style: none; position: absolute; left: 18px; top: 24px; }
  .services-list li {
    font-family: "Montserrat", sans-serif; font-weight: 600; font-size: 21.5px; color: var(--white);
    letter-spacing: 1.1px; line-height: 26px; display: flex; align-items: center; white-space: nowrap;
  }
  .services-list li::before { content: ""; width: 8px; height: 8px; border-radius: 50%; background: var(--teal); margin-right: 12px; flex: none; }

  .web-pill {
    position: absolute; left: 92px; top: 374px; width: 292px; height: 31px; border-radius: 16px; background: var(--ink-dark);
    font-family: "Montserrat", sans-serif; font-weight: 700; font-size: 14px; letter-spacing: 3px; color: var(--white);
    display: flex; align-items: center; justify-content: center;
  }

  .feature { position: absolute; top: 12px; width: 229px; height: 428px; border: 3px solid var(--ink-dark); overflow: hidden; }
  .feature-1 { left: 490px; }
  .feature-2 { left: 726px; }
  .feature-3 { left: 960px; }
  .feature-photo { position: absolute; inset: 0; }
  .feature-1 .feature-photo {
    background:
      radial-gradient(ellipse 40% 30% at 0% 45%, #5b9fd0 0%, rgba(91,159,208,0) 100%),
      radial-gradient(ellipse 45% 30% at 75% 62%, #8fb6d8 0%, rgba(143,182,216,0) 100%),
      linear-gradient(180deg, #e8ecee 0%, #d9dfe2 50%, #a9c3d8 78%, #2f5fa0 100%);
  }
  .feature-2 .feature-photo {
    background:
      radial-gradient(ellipse 30% 40% at 20% 75%, #b07a5a 0%, rgba(176,122,90,0) 100%),
      radial-gradient(ellipse 30% 20% at 70% 20%, #8a6650 0%, rgba(138,102,80,0) 100%),
      linear-gradient(170deg, #6e97d4 0%, #4b74b8 45%, #3a63a6 75%, #34548a 100%);
  }
  .feature-3 .feature-photo {
    background:
      radial-gradient(ellipse 40% 40% at 100% 85%, #d9a06c 0%, rgba(217,160,108,0) 100%),
      radial-gradient(ellipse 45% 35% at 25% 60%, #a9c3d6 0%, rgba(169,195,214,0) 100%),
      linear-gradient(160deg, #f6dcd2 0%, #e9cfd6 35%, #c9cde0 60%, #b7c6d2 100%);
  }
  .feature-caption {
    position: absolute; left: 0; right: 0; bottom: 0; height: 106px; background: var(--caption-bg);
    display: flex; align-items: center; padding-left: 13px;
    font-family: "Montserrat", sans-serif; font-weight: 700; font-size: 23px; line-height: 27px; color: var(--white); text-transform: uppercase; letter-spacing: 0.3px;
  }
  .feature-3 .feature-caption { font-size: 21px; line-height: 22.5px; padding-left: 12px; }
</style>
</head>
<body>
<main class="cover">
  <header class="brand">
    <div class="brand-mark"></div>
    <div class="brand-name"><span class="line-1">LARCHMONT</span><span class="line-2">ORTHOPAEDICS</span></div>
  </header>

  <section class="services-panel">
    <div class="services-box">
      <h2 class="services-title">SERVICES</h2>
      <ul class="services-list">
        <li>TOTAL KNEE REPLACEMENTS</li>
        <li>TOTAL HIP REPLACEMENTS</li>
        <li>SPORTS INJURY OF THE KNEE</li>
        <li>HIP FRACTURES</li>
      </ul>
    </div>
  </section>

  <div class="web-pill">WWW.WEBSITE.COM</div>

  <article class="feature feature-1">
    <div class="feature-photo" role="img" aria-label="Physiotherapist fitting a knee brace on a patient standing beside an exercise ball"></div>
    <p class="feature-caption">Patient<br>Centred<br>Care</p>
  </article>
  <article class="feature feature-2">
    <div class="feature-photo" role="img" aria-label="Clinician in blue scrubs examining a patient's lower leg"></div>
    <p class="feature-caption">Value<br>Driven</p>
  </article>
  <article class="feature feature-3">
    <div class="feature-photo" role="img" aria-label="Surgeon performing arthroscopic knee surgery in an operating theatre"></div>
    <p class="feature-caption">Double<br>Fellowship<br>Trained<br>Surgeons</p>
  </article>
</main>
</body>
</html>
```